Harlow Mailbox Services, full-service collaboration with postal service - installation of units

1. CBU - Cluster Box Unit - These are Mailbox units that you would see at residential neighborhoods, and Apartments -
2. Logo Needed
3. Maybe have CBU as a division of DWFS (Dermot Vance Field Services)
4. Card to be primary Harlow Mailbox Services

This is a letter of introduction that I am developing:

I am writing to introduce Dermot Vance Field Services, a company dedicated to delivering exceptional service and quality in the installation and maintenance of commercial mailboxes, specifically Cluster Box Units (CBUs). Our commitment to excellence and customer satisfaction has established us as a trusted partner for developers and postal services alike.
At Dermot Vance Field Services, we take pride in our comprehensive approach, ensuring that every step of the mailbox installation process is handled with precision and care. Our services include:
• Supplying high-quality CBUs tailored to meet the specific needs of your development.
• Providing a CBU plat layout upon approval of the address plat, ensuring seamless integration into your development plans.
• Collaborating with developers and postmasters to determine the optimal CBU locations for efficient mail delivery.
• Qualifying the labeling of CBU units, offering both sticker and etching options to suit your preferences.
• Pouring durable concrete foundations as required for the secure installation of the CBU units.
• Handling the installation process with expertise and attention to detail.
• Labeling the units and supplying keys for each mailbox, ensuring a smooth transition for residents and businesses.
Our team is dedicated to working closely with you to ensure that all requirements are met and that the installation process is completed efficiently and to the highest standards.
We look forward to the opportunity to collaborate with you and contribute to the success of your project. Please do not hesitate to contact us for any additional information or to discuss your specific requirements.
Sincerely,
Dermot Vance
Dermot Vance Field Services

Target Market(s)

Developers, Builders, Apartment's, HOA

Industry/Entity Type

Construction

Contact Information for Business Card

Name: Dermot Vance, Cell:555-671-0148, Email: derm@dvfieldco.example

Font styles to use
Serif

Requirements
Must have
• Fresh Looking
Nice to have
• Maybe a CBU Box if it looks clean
Should not have
• Not Industrial or Old traditional card

```html
<!DOCTYPE html>
<html lang="en">
<head>
<meta charset="utf-8">
<title>Dermot Vance Field Services – Business Card</title>
<link rel="stylesheet" href="https://fonts.googleapis.com/css2?family=Poppins:wght@400;500;600;700&display=swap">
<style>
  :root{
    --stage:#3b3b3d;
    --brand-blue:#0a4fa0;
    --brand-blue-light:#1a62b4;
    --brand-navy:#0b4a9e;
    --accent-red:#ea2b2f;
    --paper:#ffffff;
    --ink:#1b1b1f;
    --rule:#c9ccd6;
    --art-on-blue:#3a5fa8;
    --art-on-white:#d8dbef;
  }
  *{box-sizing:border-box;margin:0;padding:0}
  html,body{width:1200px;height:694px;overflow:hidden}
  body{background:var(--stage);font-family:"Poppins",sans-serif;position:relative}

  .card{position:absolute;top:192px;width:540px;height:310px;border-radius:22px;overflow:hidden}
  .card--front{left:40px;background:linear-gradient(135deg,var(--brand-blue-light) 0%,var(--brand-blue) 55%,var(--brand-blue) 100%);color:var(--paper)}
  .card--back{left:620px;background:var(--paper);color:var(--ink)}

  .brand{position:absolute;left:38px;display:flex;align-items:center;gap:14px}
  .card--front .brand{top:48px}
  .card--back .brand{top:56px}
  .brand__mark{width:48px;height:48px;flex:none}
  .card--front .brand__mark{background:var(--paper)}
  .card--back .brand__mark{background:var(--brand-navy)}
  .brand__name{font-weight:600;font-size:25px;line-height:1.1;text-transform:uppercase;white-space:nowrap}
  .card--front .brand__name{color:var(--paper)}
  .card--back .brand__name{color:var(--brand-navy)}

  .services{position:absolute;left:40px;top:150px;list-style:none;font-size:16px;line-height:25px;font-weight:400}
  .services li{display:flex;align-items:center;gap:11px;white-space:nowrap}
  .services li::before{content:"";width:10px;height:10px;background:var(--accent-red);flex:none}

  .artwork{position:absolute;right:40px;top:24px;width:150px;border-radius:4px}
  .card--front .artwork{height:230px;background:linear-gradient(180deg,var(--art-on-blue) 0%,rgba(58,95,168,.55) 100%)}
  .card--back .artwork{height:230px;background:linear-gradient(180deg,var(--art-on-white) 0%,rgba(216,219,239,.5) 100%)}

  .person{position:absolute;left:40px;top:150px}
  .person__name{font-weight:700;font-size:24px;line-height:32px;color:var(--brand-navy);text-transform:uppercase;letter-spacing:.3px}
  .person__title{font-size:14px;line-height:20px;color:var(--accent-red)}
  .person__rule{position:absolute;left:160px;top:194px;width:160px;height:1px;background:var(--rule)}

  .contact{position:absolute;left:40px;top:214px;list-style:none;font-size:13.5px;line-height:23px}
  .contact li{display:flex;align-items:center;gap:9px;white-space:nowrap}
  .contact svg{width:14px;height:14px;flex:none}
</style>
</head>
<body>

<section class="card card--front" aria-label="Card front">
  <div class="brand">
    <span class="brand__mark"></span>
    <span class="brand__name">Dermot Vance<br>Field Services</span>
  </div>
  <ul class="services">
    <li>CBU Box Layout</li>
    <li>Submittal to Postal Services</li>
    <li>Supply CBU per Postal Approval</li>
    <li>Install CBU</li>
    <li>Supply Keys</li>
  </ul>
  <div class="artwork" role="img" aria-label="Illustration of a pedestal cluster box mailbox unit"></div>
</section>

<section class="card card--back" aria-label="Card back">
  <div class="brand">
    <span class="brand__mark"></span>
    <span class="brand__name">Dermot Vance<br>Field Services</span>
  </div>
  <div class="person">
    <p class="person__name">Owen Castell</p>
    <p class="person__title">Founder &amp; CEO</p>
  </div>
  <span class="person__rule"></span>
  <ul class="contact">
    <li>
      <svg viewBox="0 0 16 16" aria-hidden="true"><path fill="#ea2b2f" d="M3.6 1.5l2.2 2.7-1.3 1.7c.9 2 2.5 3.6 4.6 4.6l1.7-1.3 2.7 2.2-1.3 2.3C6.8 13.6 2.4 9.2 1.3 3z"/></svg>
      <span>+1 555 671 0148</span>
    </li>
    <li>
      <svg viewBox="0 0 16 16" aria-hidden="true"><rect x="1" y="3" width="14" height="10" rx="1" fill="#ea2b2f"/><path d="M1.5 3.8L8 9l6.5-5.2" stroke="#fff" stroke-width="1.3" fill="none"/></svg>
      <span>info@dermotvancefield.example</span>
    </li>
    <li>
      <svg viewBox="0 0 16 16" aria-hidden="true"><circle cx="8" cy="8" r="7" fill="#ea2b2f"/><path d="M1 8h14M8 1c-3 3.5-3 10.5 0 14M8 1c3 3.5 3 10.5 0 14" stroke="#fff" stroke-width="1" fill="none"/></svg>
      <span>www.dermotvancefield.example</span>
    </li>
  </ul>
  <div class="artwork" role="img" aria-label="Faint illustration of a pedestal cluster box mailbox unit"></div>
</section>

</body>
</html>
```